Biz card for my counselling/social work practice

Biz card design for my counselling practice, focus on well-being, I am a social worker who also teaches meditation and workshops but my main focus for the card is my counselling practice. My website reveals a gentle flowing quality which I would life reflected in my card. This business card will be designed to share with other practitioners who are looking for support with their clients to take their healing to another level or well-being.

Target Market(s)

professionals seeking mental health counselling/men/women/ those seeking to improve their well-being through insight based counselling to optimize their lives and process trauma or limiting patterns

Industry/Entity Type

Counsellor

Contact Information for Business Card

Info on the card: perhaps text is aligned left?
Maribel Strand, MSW, RSW
Counsellor
614.295.3140
info@maribelstrand.example
www.maribelstrand.example

Please use a modern font doesn’t need to be the one chosen below. Thank you

Font styles to use
Serif

Colors
3176b5
33a6d7
33b8a4
6b449b
abd037
d2a4cc
e55fa2

Requirements
Must have
• My business card details on front
• Backside
• Accelerated Resolution Therapy
• Cognitive Behavioral Therapy
• Mindfulness Informed Therapy
Nice to have
• I would like the card to be basic, (white or creme without too much bold colour) and with perhaps a stripe or band of vertical colour in blue or green (or a merge of colour) perhaps embossed or in a negative space. (this is one idea, but do not want the card to be too feminine or interest only women as i see men too so this is only an idea, but not 100 percent on this.
• I do not have a logo. I would prefer to heart from my website not to be used in the design as i am considering modifying this and re-branding.
Should not have
• too bold colours or bright yellow/blacks. i Like tones that are greens, blues.

```html
<!DOCTYPE html>
<html lang="en">
<head>
<meta charset="utf-8">
<title>Maribel Strand – Counsellor Business Card</title>
<link rel="stylesheet" href="https://fonts.googleapis.com/css2?family=Quicksand:wght@300;400;500;700&display=swap">
<style>
  :root {
    --page-bg: #e6e9ec;
    --card-bg: #ffffff;
    --blue-dark: #3176b5;
    --blue-light: #33a6d7;
    --teal: #33b8a4;
    --green: #abd037;
    --card-shadow: rgba(30, 40, 50, 0.16);
  }
  * { box-sizing: border-box; margin: 0; padding: 0; }
  html, body {
    width: 1200px;
    height: 900px;
    overflow: hidden;
    background: var(--page-bg);
    font-family: "Quicksand", sans-serif;
  }
  .sheet {
    width: 1200px;
    height: 900px;
    display: flex;
    align-items: center;
    justify-content: center;
    gap: 60px;
  }
  .card {
    position: relative;
    width: 525px;
    height: 300px;
    background: var(--card-bg);
    border-radius: 26px;
    overflow: hidden;
    box-shadow: 0 10px 28px var(--card-shadow);
  }
  .card__band {
    position: absolute;
    left: 0; top: 0; bottom: 0;
    width: 44px;
  }
  .card--front .card__band { background: var(--blue-light); }
  .card--back .card__band { background: var(--green); }

  .band-mark {
    position: absolute;
    left: 10px;
    bottom: 20px;
    width: 24px;
    height: 24px;
    border-radius: 50%;
    background: var(--card-bg);
  }

  /* Front side */
  .identity {
    position: absolute;
    right: 32px;
    top: 34px;
    text-align: right;
  }
  .identity__name {
    font-size: 25px;
    color: var(--blue-dark);
    font-weight: 400;
    line-height: 1.15;
  }
  .identity__name strong { font-weight: 700; }
  .identity__role {
    font-size: 19px;
    color: var(--blue-light);
    font-weight: 400;
    margin-top: 2px;
  }
  .contacts {
    position: absolute;
    right: 32px;
    bottom: 30px;
    list-style: none;
    display: flex;
    flex-direction: column;
    gap: 8px;
  }
  .contacts__item {
    display: flex;
    align-items: center;
    justify-content: flex-end;
    gap: 14px;
    font-size: 17px;
    color: var(--blue-light);
    font-weight: 500;
  }
  .contacts__icon {
    width: 24px;
    height: 24px;
    flex: none;
  }

  /* Back side */
  .services {
    position: absolute;
    left: 110px;
    top: 70px;
    list-style: none;
    display: flex;
    flex-direction: column;
    gap: 4px;
  }
  .services__item {
    display: flex;
    align-items: center;
    gap: 14px;
    font-size: 21px;
    font-weight: 300;
    color: var(--green);
    letter-spacing: 0.2px;
  }
  .services__bullet {
    width: 14px;
    height: 14px;
    border-radius: 50%;
    background: var(--green);
    flex: none;
  }
</style>
</head>
<body>
  <main class="sheet">
    <!-- Front -->
    <section class="card card--front" aria-label="Business card front">
      <div class="card__band"><span class="band-mark"></span></div>
      <div class="identity">
        <p class="identity__name"><strong>Maribel Strand</strong>, MSW, RSW</p>
        <p class="identity__role">Counsellor</p>
      </div>
      <ul class="contacts">
        <li class="contacts__item">
          <span>614.295.3140</span>
          <svg class="contacts__icon" viewBox="0 0 24 24" aria-hidden="true">
            <circle cx="12" cy="12" r="12" fill="var(--teal)"/>
            <path d="M8.6 6.5c.4-.3 1-.2 1.2.2l1.1 2c.2.4.1.8-.2 1.1l-.7.6c.6 1.3 1.6 2.3 2.9 2.9l.6-.7c.3-.3.7-.4 1.1-.2l2 1.1c.4.2.5.8.2 1.2l-.9 1c-.6.6-1.5.8-2.3.4-2.6-1.2-4.6-3.2-5.8-5.8-.4-.8-.2-1.7.4-2.3z" fill="#fff"/>
          </svg>
        </li>
        <li class="contacts__item">
          <span>info@maribelstrand.example</span>
          <svg class="contacts__icon" viewBox="0 0 24 24" aria-hidden="true">
            <circle cx="12" cy="12" r="12" fill="var(--green)"/>
            <rect x="6" y="8" width="12" height="8.5" rx="1" fill="none" stroke="#fff" stroke-width="1.4"/>
            <path d="M6.5 8.6 12 13l5.5-4.4" fill="none" stroke="#fff" stroke-width="1.4"/>
          </svg>
        </li>
        <li class="contacts__item">
          <span>www.maribelstrand.example</span>
          <svg class="contacts__icon" viewBox="0 0 24 24" aria-hidden="true">
            <circle cx="12" cy="12" r="12" fill="var(--teal)"/>
          </svg>
        </li>
      </ul>
    </section>

    <!-- Back -->
    <section class="card card--back" aria-label="Business card back">
      <div class="card__band"></div>
      <ul class="services">
        <li class="services__item"><span class="services__bullet"></span>Accelerated Resolution Therapy</li>
        <li class="services__item"><span class="services__bullet"></span>Cognitive Behavioral Therapy</li>
        <li class="services__item"><span class="services__bullet"></span>Mindfulness Informed Therapy</li>
      </ul>
    </section>
  </main>
</body>
</html>
```